Paws and Meadows is a dog walking service that offers home boarding and pet taxi

I am looking for a eye catching A5 leaflet/flyer design for my dog walking business Paws and Meadows.

The flyer must have my company logo on it (jpeg), a picture of my van (jpeg) and a picture of dogs playing (jpegs 1-5).

The fonts must be easy to read. I am not set on any colour scheme but do like the idea of having a natural background. IE. Green grass and blue sky or some forest setting with green trees. If you don't like this idea or its hard to work with don't worry I am open minded so be creative and do what you thinks best.

I'll provide quick feedback to designs that i like and so we can work together.

The flyers must contain the following:

60 minute group and individual walks
GPS Tracked Walks
Home Boarding
Pet Taxi
Puppy/Pet visits

Offer: 50% off first weeks dogs walks with this flyer.

As well as containing my contact info:

07915382046
www.paws-and-meadows.co.uk
paws-and-meadows@mailbrook.co.uk

Chatterbook, Chirpline and Snapgallery logos must be present as well.

Thanks and Good luck!

Target Market(s)

ANYONE WHO NEEDS THEIR DOG WALKED OR LOOKED AFTER WHEN THEY ARE ON HOLIDAY

Industry/Entity Type

Business

Contact Information for Business Card

THE BUSINESS CARD MUST DISPLAY THE LOGO THAT HAS BEEN UPLOADED IN A FILE. IT MUST LOOK SHARP AND PROFESSIONAL. CONTAIN ALL CONTACT INFO AND HAVE SERVICES OFFERED. SEE PROJECT DESCRIPTION FOR FLYER.

Font styles to use
Serif
Sans Serif

Requirements
Must have
• SEE PROJECT DESCRIPTION
Nice to have
• IT WOULD BE NICE TO HAVE PHOTOS OF MY VAN AND DOGS PLAYING. I HAVE UPLOADED SOME PICS OF VAN TO BE USED AND THERE ARE PICS OF DOGS PLAYING THAT COULD BE USED.

```html
<!DOCTYPE html>
<html lang="en">
<head>
<meta charset="utf-8">
<title>Paws and Meadows – Dog Walking Service Flyer</title>
<link href="https://fonts.googleapis.com/css2?family=Nunito:wght@800;900&display=swap" rel="stylesheet">
<style>
  :root {
    --sky-top: #3f8fd6;
    --sky-bottom: #8ec3ea;
    --grass-light: #6fb83a;
    --grass-dark: #3f8a1e;
    --ink: #1f1f1f;
    --white: #ffffff;
    --offer-gold: #e2ab4b;
    --offer-border: #2a2a2a;
    --gap: #ffffff;
  }
  * { margin: 0; padding: 0; box-sizing: border-box; }
  html, body { width: 1200px; height: 847px; overflow: hidden; background: var(--white); }
  body { font-family: "Nunito", Arial, sans-serif; }

  .flyer { position: relative; width: 1200px; height: 847px; overflow: hidden; background: var(--gap); }

  .main-panel { position: absolute; left: 0; top: 0; width: 798px; height: 847px; overflow: hidden; }
  .sky { position: absolute; left: 0; top: 0; width: 100%; height: 564px;
         background: linear-gradient(to bottom, var(--sky-top), var(--sky-bottom)); }
  .meadow { position: absolute; left: 0; top: 564px; width: 100%; height: 283px;
            background: linear-gradient(to bottom, var(--grass-light), var(--grass-dark)); }

  .brand-name { position: absolute; left: 0; top: 208px; width: 798px; text-align: center;
    font-size: 50px; font-weight: 900; color: var(--ink); line-height: 1; }

  .services { position: absolute; left: 0; top: 348px; width: 798px; list-style: none; text-align: center; }
  .services li { font-size: 25px; font-weight: 900; color: var(--ink); line-height: 29px; letter-spacing: 0.4px; }

  .contact { position: absolute; left: 58px; top: 622px; list-style: none; }
  .contact li { font-size: 22px; font-weight: 900; color: var(--white); line-height: 29px; }

  .social { position: absolute; left: 556px; top: 638px; list-style: none; }
  .social li { display: flex; align-items: center; gap: 10px; font-size: 17px; font-weight: 900;
    color: var(--white); line-height: 24px; margin-bottom: 4px; }
  .social li::before { content: ""; width: 18px; height: 18px; border-radius: 50%; background: var(--white); }

  .offer { position: absolute; left: 30px; top: 750px; width: 738px; height: 66px;
    background: var(--offer-gold); border: 3px dashed var(--offer-border);
    display: flex; align-items: center; padding-left: 26px;
    font-size: 23px; font-weight: 900; color: var(--ink); }

  .photo-column { position: absolute; left: 802px; top: 0; width: 398px; height: 847px; }
  .photo { position: absolute; left: 0; width: 398px; height: 280px; }
  .photo-dogs-stick { top: 0; background: linear-gradient(135deg, #7aa54a 0%, #b08a55 45%, #2b2a26 75%, #6f9a40 100%); }
  .photo-dogs-water { top: 283px; background: linear-gradient(to bottom, #d9dde2 0%, #8c8a80 35%, #5c636a 70%, #3d3f41 100%); }
  .photo-van { top: 566px; height: 281px; background: linear-gradient(to bottom, #7fb4e6 0%, #e9eef2 45%, #c9c6bd 80%, #8a8a82 100%); }
</style>
</head>
<body>
<div class="flyer">
  <section class="main-panel">
    <div class="sky"></div>
    <div class="meadow"></div>

    <div class="brand-name">Paws and Meadows</div>

    <ul class="services">
      <li>60 minute group and individual walks</li>
      <li>GPS Tracked Walks</li>
      <li>Home Boarding</li>
      <li>Pet Taxi</li>
      <li>Puppy/Pet visits</li>
    </ul>

    <ul class="contact">
      <li>07915382046</li>
      <li>www.paws-and-meadows.co.uk</li>
      <li>paws-and-meadows@mailbrook.co.uk</li>
    </ul>

    <ul class="social">
      <li>Chatterbook</li>
      <li>Chirpline</li>
      <li>Snapgallery</li>
    </ul>

    <div class="offer">Offer: 50% off first weeks dogs walks with this flyer.</div>
  </section>

  <aside class="photo-column">
    <div class="photo photo-dogs-stick" role="img" aria-label="Photo: two dogs running on grass carrying a stick together"></div>
    <div class="photo photo-dogs-water" role="img" aria-label="Photo: three dogs splashing through shallow water"></div>
    <div class="photo photo-van" role="img" aria-label="Photo: the branded dog walking van parked outdoors"></div>
  </aside>
</div>
</body>
</html>
```